Brightvale Landscape & Construction Website

I have created a detailed txt document and included it in the files upload that will provide all the project details because trying to list it in here is cumbersome. This is for a website only. I have my own team to handle the psd to html conversion. They have an existing website which I have added in the doc. I have also upload various logo files to be used.

Industry/Entity Type

Landscape and Construction

Number of Pages Required

1 page

```html
<!DOCTYPE html>
<html lang="en">
<head>
<meta charset="utf-8">
<title>Brightvale Landscape & Construction</title>
<link href="https://fonts.googleapis.com/css2?family=Montserrat:wght@400;500;600;700&display=swap" rel="stylesheet">
<style>
:root{
  --black:#0d0d0d;
  --orange:#f7941d;
  --yellow:#fbc13a;
  --gold:#f5b21b;
  --white:#ffffff;
  --grey-bg:#f3f3f3;
  --text:#1e1e1e;
  --muted:#555;
}
*{margin:0;padding:0;box-sizing:border-box}
html,body{width:1200px;height:4085px;overflow:hidden}
body{position:relative;font-family:'Montserrat',sans-serif;color:var(--text);background:var(--white)}
.abs{position:absolute}
.topbar{left:0;top:0;width:1200px;height:104px;background:var(--black)}
.brand{left:66px;top:22px;display:flex;align-items:center;gap:10px;color:var(--orange);font-weight:700;font-size:21px}
.brand-dot{width:26px;height:26px;border-radius:50%;background:var(--orange)}
.contact-mini{top:26px;color:var(--white);font-size:11px;line-height:1.35}
.contact-mini b{color:var(--orange);font-weight:600;display:block}
.socials{left:1044px;top:28px;display:flex;gap:8px}
.socials span{width:15px;height:15px;border-radius:50%;background:var(--white)}
.nav{left:92px;top:73px;width:1038px;height:62px;background:var(--white);display:flex;align-items:center;padding:0 30px;gap:0;box-shadow:0 2px 8px rgba(0,0,0,.15);z-index:3}
.nav a{font-size:12px;font-weight:600;color:var(--text);text-decoration:none;margin-right:34px;letter-spacing:.2px}
.nav a.active{color:var(--orange)}
.quote-btn{margin-left:auto;background:var(--gold);color:var(--text);font-size:12px;font-weight:600;padding:9px 20px}
.hero{left:0;top:104px;width:1200px;height:562px;background:linear-gradient(180deg,#8a9098 0%,#a9a6a0 35%,#7b7264 62%,#4d6a2f 82%,#6a8a3a 100%)}
.hero-arrow{width:40px;height:40px;border:1.5px solid var(--white);border-radius:50%;display:flex;align-items:center;justify-content:center}
.hero-caption{left:0;width:1200px;top:545px;text-align:center;color:var(--white);font-size:26px;font-weight:400;letter-spacing:.5px}
.dots{display:flex;gap:6px}
.dots i{width:10px;height:10px;border-radius:50%;border:1.5px solid #999;display:block}
.dots i.on{background:var(--gold);border-color:var(--gold)}
.hero .dots i{border-color:var(--white)}
.band{top:666px;height:157px;width:600px;display:flex;align-items:center;justify-content:center;gap:12px;font-size:21px;font-weight:600;color:var(--text)}
.band-left{left:0;background:var(--orange)}
.band-right{left:600px;background:var(--yellow)}
.welcome-img{left:76px;top:907px;width:447px;height:285px;background:linear-gradient(160deg,#7f8a8e 0%,#9a8f80 40%,#8d8a86 70%,#6f7a5a 100%)}
.welcome-kicker{left:571px;top:928px;font-size:15px;font-weight:500}
.welcome-title{left:571px;top:957px;font-size:24px;font-weight:500}
.welcome-copy{left:568px;top:1000px;width:528px;font-size:11.2px;line-height:1.69;color:var(--text)}
.sec-title{left:0;width:1200px;text-align:center;font-size:23px;font-weight:500}
.sec-sub{left:0;width:1200px;text-align:center;font-size:12px}
.card{width:137px;background:var(--white);text-align:center;font-size:14px;line-height:1.2}
.card .thumb{height:82px}
.card .label{height:70px;display:flex;align-items:center;justify-content:center;padding:0 6px}
.card.raised{box-shadow:0 12px 22px rgba(0,0,0,.18)}
.arrow{width:24px;height:24px}
.grey{left:0;top:1628px;width:1200px;height:425px;background:var(--grey-bg)}
.service-band{left:0;top:2053px;width:1200px;height:405px;background:linear-gradient(120deg,#3d4b2c 0%,#4e6a2e 40%,#3f5d25 100%)}
.service-title{left:133px;top:2244px;color:var(--white);font-size:31px;font-weight:500}
.map{left:525px;top:2105px;width:608px;height:474px;background:linear-gradient(135deg,#ece8df 0%,#e4e8df 60%,#cfe4f0 85%,#9fd3ef 100%);border:1px solid #ddd}
.gal{background:#888}
.gal-caption{left:449px;top:2880px;width:302px;text-align:center;color:var(--white);font-size:20px;line-height:1.2}
.gal-btn{left:512px;top:3373px;width:177px;height:33px;background:var(--orange);color:var(--text);font-size:12px;font-weight:600;display:flex;align-items:center;justify-content:center}
.footer-bg{left:0;top:3475px;width:1200px;height:465px}
.foot-title{left:119px;top:3566px;color:var(--white);font-size:22px;font-weight:700}
.foot-copy{left:119px;top:3616px;width:370px;color:var(--white);font-size:11.5px;line-height:1.8}
.foot-addr{left:122px;top:3728px;color:var(--white);font-size:11.5px;line-height:1.85}
.foot-addr b{font-weight:600}
.field{left:693px;width:348px;background:var(--white);border:1px solid #ccc;font-size:11px;color:#999;padding:12px 16px}
.send{left:697px;top:3831px;width:89px;height:29px;background:var(--orange);color:var(--text);font-size:11.5px;font-weight:600;display:flex;align-items:center;justify-content:center}
.foot-links{left:79px;top:3967px;display:flex;gap:15px;font-size:12px;font-weight:500}
.badge{top:3956px;height:46px;border-radius:4px}
.rule{left:63px;top:4021px;width:1070px;height:1px;background:#ccc}
.legal{left:0;width:1200px;top:4047px;text-align:center;font-size:9.5px;color:#333}
</style>
</head>
<body>

<header class="abs topbar"></header>
<div class="abs brand"><span class="brand-dot"></span>BRIGHTVALE LANDSCAPE &amp; CONSTRUCTION</div>
<div class="abs contact-mini" style="left:712px">
  <svg width="16" height="14" viewBox="0 0 16 14" style="position:absolute;left:-22px;top:2px"><path d="M3 1h3l1 3-2 1a8 8 0 0 0 4 4l1-2 3 1v3c0 1-1 2-2 2C6 13 1 8 1 3c0-1 1-2 2-2z" fill="#fff"/></svg>
  <b>555-204-7310</b>Make a Call</div>
<div class="abs contact-mini" style="left:845px"><b>dan@brightvalelandscape.com</b>Drop us a line</div>
<div class="abs socials"><span></span><span></span><span></span><span></span></div>

<nav class="abs nav">
  <a class="active">HOME</a><a>LANDSCAPE SERVICES</a><a>CONSTRUCTION&nbsp; SERVICES</a><a>COMPANY</a><a>CONTACT</a><a>FAQS</a><a>GALLERY</a>
  <span class="quote-btn">GET A QUOTE</span>
</nav>

<section class="abs hero" role="img" aria-label="Photo of a stucco house with flower baskets, fresh mulch beds and a green lawn">
  <div class="abs hero-arrow" style="left:64px;top:269px"><svg width="14" height="12" viewBox="0 0 14 12"><path d="M13 6H2M6 1 1 6l5 5" stroke="#fff" stroke-width="1.5" fill="none"/></svg></div>
  <div class="abs hero-arrow" style="left:1093px;top:269px"><svg width="14" height="12" viewBox="0 0 14 12"><path d="M1 6h11M8 1l5 5-5 5" stroke="#fff" stroke-width="1.5" fill="none"/></svg></div>
  <div class="abs hero-caption" style="top:441px">General Landscaping &nbsp;<svg width="14" height="12" viewBox="0 0 14 12"><path d="M1 6h11M8 1l5 5-5 5" stroke="#fff" stroke-width="1.5" fill="none"/></svg></div>
  <div class="abs dots" style="left:578px;top:513px"><i class="on"></i><i></i><i></i></div>
</section>

<div class="abs band band-left">
  <svg width="30" height="26" viewBox="0 0 30 26"><circle cx="9" cy="6" r="4" fill="#1e1e1e"/><circle cx="21" cy="6" r="4" fill="#1e1e1e"/><path d="M1 24c0-7 4-11 8-11s8 4 8 11zM13 24c0-7 4-11 8-11s8 4 8 11z" fill="#1e1e1e"/></svg>
  Landscape Services&nbsp;
  <svg width="14" height="12" viewBox="0 0 14 12"><path d="M1 6h11M8 1l5 5-5 5" stroke="#1e1e1e" stroke-width="1.5" fill="none"/></svg>
</div>
<div class="abs band band-right">
  <svg width="30" height="30" viewBox="0 0 30 30"><path d="M3 16a12 12 0 0 1 24 0z" fill="#1e1e1e"/><rect x="1" y="17" width="28" height="4" fill="#1e1e1e"/><path d="M8 23a7 6 0 0 0 14 0z" fill="#1e1e1e"/></svg>
  Construction Services&nbsp;
  <svg width="14" height="12" viewBox="0 0 14 12"><path d="M1 6h11M8 1l5 5-5 5" stroke="#1e1e1e" stroke-width="1.5" fill="none"/></svg>
</div>

<div class="abs welcome-img" role="img" aria-label="Photo of workers laying a paver driveway in front of a house"></div>
<p class="abs welcome-kicker">Welcome to</p>
<h1 class="abs welcome-title">Brightvale Landscape &amp; Construction Inc</h1>
<p class="abs welcome-copy">Lorem ipsum dolor sit amet consectetur. Nisl volutpat cras faucibus orci orci nibh placerat. Consectetur nisl praesent pretium ac interdum pellentesque nunc nulla lacus. Faucibus neque pretium nunc nec nibh neque vitae nullam nascetur. Eleifend eget faucibus nibh quis. Eleifend leo in in sed felis. Nibh ut imperdiet lectus purus. Pulvinar neque maecenas dis tellus. Mauris fermentum varius aenean mauris montes. Scelerisque gravida at orci justo leo nunc donec ultricies. Tempor ullamcorper convallis pellentesque sapien. Elementum integer vel velit egestas elementum nunc eu ultrices. Nisl tortor urna tortor sit diam velit libero sit volutpat.</p>

<h2 class="abs sec-title" style="top:1277px">Landscaping Services</h2>
<p class="abs sec-sub" style="top:1318px">Lorem ipsum dolor sit amet consectetur. Ut massa nullam adipiscing.</p>
<svg class="abs arrow" style="left:67px;top:1435px" viewBox="0 0 24 24"><path d="M21 12H4M10 5l-7 7 7 7" stroke="#1e1e1e" stroke-width="1.8" fill="none"/></svg>
<svg class="abs arrow" style="left:1112px;top:1435px" viewBox="0 0 24 24"><path d="M3 12h17M14 5l7 7-7 7" stroke="#1e1e1e" stroke-width="1.8" fill="none"/></svg>
<div class="abs card raised" style="left:130px;top:1370px"><div class="thumb" role="img" aria-label="Photo of a brick paver patio" style="background:linear-gradient(160deg,#b9694a,#8e4a35)"></div><div class="label">Paver Patios/ Driveways</div></div>
<div class="abs card" style="left:290px;top:1370px"><div class="thumb" role="img" aria-label="Photo of a boulder retaining wall" style="background:linear-gradient(160deg,#9b9486,#6d6a4f)"></div><div class="label">Retaining/ Boulder Walls</div></div>
<div class="abs card" style="left:452px;top:1370px"><div class="thumb" role="img" aria-label="Photo of a garden pond with flowers" style="background:linear-gradient(160deg,#5c8a3c,#a8624a)"></div><div class="label">Ponds</div></div>
<div class="abs card" style="left:612px;top:1370px"><div class="thumb" role="img" aria-label="Photo of a rock waterfall" style="background:linear-gradient(160deg,#6f6e68,#3f3e39)"></div><div class="label">Waterfalls</div></div>
<div class="abs card" style="left:772px;top:1370px"><div class="thumb" role="img" aria-label="Photo of fresh sod lawn" style="background:linear-gradient(160deg,#6f9a4a,#4d7a2a)"></div><div class="label">Sod</div></div>
<div class="abs card" style="left:932px;top:1370px"><div class="thumb" role="img" aria-label="Photo of a graded yard beside a house" style="background:linear-gradient(160deg,#a39a8a,#6c7a4c)"></div><div class="label">Grading/ Excavating</div></div>
<div class="abs dots" style="left:578px;top:1552px"><i class="on"></i><i></i><i></i></div>

<section class="abs grey"></section>
<h2 class="abs sec-title" style="top:1672px">Construction Services</h2>
<p class="abs sec-sub" style="top:1710px">Lorem ipsum dolor sit amet consectetur. Ut massa nullam adipiscing.</p>
<svg class="abs arrow" style="left:65px;top:1841px" viewBox="0 0 24 24"><path d="M21 12H4M10 5l-7 7 7 7" stroke="#1e1e1e" stroke-width="1.8" fill="none"/></svg>
<svg class="abs arrow" style="left:1110px;top:1841px" viewBox="0 0 24 24"><path d="M3 12h17M14 5l7 7-7 7" stroke="#1e1e1e" stroke-width="1.8" fill="none"/></svg>
<div class="abs card" style="left:128px;top:1777px"><div class="thumb" role="img" aria-label="Photo of a two-level deck" style="background:linear-gradient(160deg,#8a8a7a,#5c5442)"></div><div class="label">Decks</div></div>
<div class="abs card" style="left:288px;top:1777px"><div class="thumb" role="img" aria-label="Photo of a house with new footings" style="background:linear-gradient(160deg,#c9c6bd,#8f8a7c)"></div><div class="label">Footings</div></div>
<div class="abs card" style="left:450px;top:1777px"><div class="thumb" role="img" aria-label="Photo of an addition under construction" style="background:linear-gradient(160deg,#8a9a6a,#8e7a66)"></div><div class="label">Additions</div></div>
<div class="abs card" style="left:610px;top:1777px"><div class="thumb" role="img" aria-label="Photo of a white pole barn" style="background:linear-gradient(160deg,#b8c7d6,#e7e3dc 60%,#6b8a4a)"></div><div class="label">Pole barns</div></div>
<div class="abs card" style="left:770px;top:1777px"><div class="thumb" role="img" aria-label="Photo of a lakeside cabin" style="background:linear-gradient(160deg,#8a7a3a,#a65a2a)"></div><div class="label">Cabins</div></div>
<div class="abs card" style="left:930px;top:1777px"><div class="thumb" role="img" aria-label="Photo of a remodeled room with stone fireplace" style="background:linear-gradient(160deg,#9a6a3a,#5a4030)"></div><div class="label">Remodels</div></div>
<div class="abs dots" style="left:573px;top:1975px"><i class="on"></i><i></i><i></i></div>

<section class="abs service-band" role="img" aria-label="Photo of a person pushing a lawn mower across grass"></section>
<h2 class="abs service-title">Service Area</h2>
<div class="abs map" role="img" aria-label="Street map of the service area with three red location pins"></div>

<h2 class="abs sec-title" style="top:2642px">Project Gallery</h2>
<div class="abs gal" role="img" aria-label="Photo of a raised deck with stairs" style="left:120px;top:2717px;width:303px;height:196px;background:linear-gradient(170deg,#c4ccd4,#bcb6a6 50%,#5e8a3a)"></div>
<div class="abs gal" role="img" aria-label="Photo of a house with a terraced block wall" style="left:120px;top:2937px;width:303px;height:380px;background:linear-gradient(170deg,#b7c2cc,#a9a690 45%,#5f8a3a)"></div>
<div class="abs gal" role="img" aria-label="Photo of a cedar deck in the woods" style="left:449px;top:2717px;width:302px;height:380px;background:linear-gradient(170deg,#4a4a3a,#6a5e4a 60%,#8a7a62)"></div>
<div class="abs gal-caption">Cedar Decks,<br>Treated Decks &amp;<br>Additions</div>
<div class="abs gal" role="img" aria-label="Photo of a garden pond with plants" style="left:449px;top:3121px;width:302px;height:196px;background:linear-gradient(170deg,#a9a39a,#4a5a3a 60%,#2a3a4a)"></div>
<div class="abs gal" role="img" aria-label="Photo of a backyard patio with a swing" style="left:778px;top:2717px;width:303px;height:196px;background:linear-gradient(170deg,#c6ccd2,#9a8a74 50%,#5e8a3a)"></div>
<div class="abs gal" role="img" aria-label="Photo of a wood-paneled cabin interior" style="left:778px;top:2937px;width:303px;height:380px;background:linear-gradient(170deg,#c89a5a,#a8743a 60%,#7a5a3a)"></div>
<div class="abs gal-btn">VIEW ALL GALLERY</div>

<svg class="abs footer-bg" viewBox="0 0 1200 465" preserveAspectRatio="none">
  <path d="M0 36 L600 0 L1200 36 L1200 52 L600 18 L0 52 Z" fill="var(--gold)"/>
  <path d="M0 52 L600 18 L1200 52 L1200 465 L0 465 Z" fill="var(--black)"/>
</svg>
<h2 class="abs foot-title">CONTACT US</h2>
<p class="abs foot-copy">We look forward to hearing about your project! Provide us with some information below, and we will be sure to get right back to you.</p>
<p class="abs foot-addr">4120 - 118th Ave NE Cedar Ridge, MN 55990<br>Phone: <b>555-204-7310</b><br>Fax: <b>555-204-7311</b><br>Email: <b>dan@brightvalelandscape.com</b></p>
<div class="abs field" style="top:3547px;height:39px">Name</div>
<div class="abs field" style="top:3600px;height:39px">Phone</div>
<div class="abs field" style="top:3652px;height:39px">Email</div>
<div class="abs field" style="top:3706px;height:106px">How can we help?</div>
<div class="abs send">SEND</div>

<nav class="abs foot-links"><span>Home</span><span>About Us</span><span>Service We Provide</span><span>Testimonials</span><span>Contact Us</span></nav>
<div class="abs badge" style="left:745px;width:118px;background:#d8dde4"></div>
<div class="abs badge" style="left:886px;width:150px;background:#cfd8e6"></div>
<div class="abs badge" style="left:1063px;width:70px;background:#cfe2cf"></div>
<div class="abs rule"></div>
<p class="abs legal">License#BC482157 &nbsp;|&nbsp; Copyright © 2022 Brightvale Landscape &amp; Construction Inc. All Rights Reserved</p>

</body>
</html>
```